flatmoveria.co.uk landing page website design

Hi designers, I would like a custom designed landing page very similar to www.dwellotrade.co.uk. It represents a happy place, sunny days and people swapping homes. I would like this done just like theres but our own design but a similar layout as theres.

I would like the 3 reasons to use us to be

Connect to thousands of other people in your area looking for a home swap

Our service is Completely free unlike most other exchange websites.

Find a exchange within 30 days!*

Thank you all,

Hi Everyone, I need the designs to represent london if possible like one of the designers has done for anyone else being in with a chance to win. Please check out the design by RT with the london look. I still like some of the others and they may win but i need to give this a try please.

Council house tenants

• Custom designed landing page showing all the elements that www.dwellotrade.co.uk use, The blue sky, and the land it shows with houses and people representing people swapping house. It can not be the same as them but can be similar concept with our own custom design and colour scheme ect.

please create 3 bubbles for speech from people. Please add the following quotes. "Its time we upsize"
"lets try and downsize and save money" "shall we move house?"
Would like 2 blocks of flats in a similar way dwello trade.co.uk show the houses.

• Same colour scheme as dwello trade apart from the blue sky

```html
<!DOCTYPE html>
<html lang="en">
<head>
<meta charset="utf-8">
<title>flatmoveria.co.uk – Swap your social home</title>
<link rel="stylesheet" href="https://fonts.googleapis.com/css2?family=Questrial&family=Montserrat:wght@600;700&display=swap">
<style>
:root{
  --green:#3bb54a;
  --green-dark:#2ea640;
  --green-bright:#45c552;
  --black:#000;
  --white:#fff;
  --ink:#1a1a1a;
  --sky-top:#8fd3d4;
  --sky-low:#a6dedd;
  --tree:#3f8a2c;
  --soil:#6a4529;
  --soil-dark:#4b2f1b;
}
*{box-sizing:border-box;margin:0;padding:0}
html,body{width:1200px;height:2178px;overflow:hidden}
body{position:relative;font-family:"Questrial",Arial,sans-serif;color:var(--white);background:var(--black)}
.scene{position:absolute;left:0;top:0;width:1200px;height:2178px;
  background:linear-gradient(180deg,var(--sky-top) 0,var(--sky-low) 420px,#7fbf8a 560px,var(--tree) 660px,#5c7a35 760px,var(--soil) 960px,#5b3b22 1250px,var(--soil-dark) 1500px,#2a1a0f 1640px,#0a0603 1720px,var(--black) 1760px)}
.abs{position:absolute}
.brand{font-family:"Questrial",Arial,sans-serif;font-weight:400;letter-spacing:-.5px}
.brand-top{left:0;width:1200px;top:56px;text-align:center;font-size:36px;color:var(--ink)}
.brand-top .dot,.brand-foot .dot{display:inline-block;width:30px;height:30px;background:var(--green);vertical-align:-4px;margin-right:12px}
.tagline{left:0;width:1200px;top:145px;text-align:center;font-size:31px;color:var(--ink)}
.search{left:144px;top:230px;width:912px;height:125px;background:var(--green)}
.search label{position:absolute;top:22px;font-size:17px;color:var(--white)}
.field{position:absolute;top:58px;width:228px;height:44px;background:var(--white);font-size:14px;color:#888;padding:14px 0 0 20px}
.field .caret{position:absolute;right:18px;top:20px;width:0;height:0;border-left:5px solid transparent;border-right:5px solid transparent;border-top:5px solid #666}
.search-btn{position:absolute;left:731px;top:58px;width:160px;height:44px;background:var(--black);color:var(--white);font-size:17px;text-align:center;line-height:44px}
.headline{left:0;width:1200px;top:420px;text-align:center;font-size:41px;line-height:51px;font-weight:400;text-shadow:0 2px 4px rgba(0,0,0,.45)}
.role-buttons{left:283px;top:583px;width:635px;height:55px;display:flex;border-radius:28px;overflow:hidden;font-family:"Montserrat",Arial,sans-serif;font-weight:600;font-size:16px}
.role-buttons span{display:flex;align-items:center;justify-content:center}
.role-tenant{width:315px;background:linear-gradient(90deg,var(--green-bright),var(--green))}
.role-landlord{flex:1;background:var(--black)}
.need-card{height:232px;top:719px;background:var(--green-dark);border-radius:0 80px 80px 0}
.need-photo{width:270px;height:270px;border-radius:50%;top:702px;border:14px solid var(--green-dark)}
.need-text{font-size:31px;line-height:36px}
.why{left:0;width:1200px;top:1064px;text-align:center;font-family:"Montserrat",Arial,sans-serif;font-weight:700;font-size:48px;line-height:55px;text-shadow:0 2px 4px rgba(0,0,0,.4)}
.reason{text-align:center;font-size:20px;line-height:27px}
.reason-mark{width:220px;height:140px}
.footer-edge{left:0;top:1680px;width:1200px;height:120px}
.foot-head{top:1760px;font-size:23px;font-weight:400;color:var(--green);letter-spacing:.5px}
.foot-list{top:1808px;font-size:14.5px;line-height:26.5px;list-style:none}
.contact-row{display:flex;gap:10px;align-items:flex-start;margin-bottom:14px;line-height:25px;font-size:14.5px}
.contact-row svg{flex:none;margin-top:6px}
.brand-foot{left:207px;top:2016px;font-size:36px;color:var(--white)}
.social{top:2016px;width:42px;height:42px;border:2px solid var(--white);border-radius:50%}
.copyright{left:0;width:1200px;top:2122px;text-align:center;font-size:13.5px}
</style>
</head>
<body>
<div class="scene" role="img" aria-label="Illustrated sunny landscape: blue sky, trees, palm trees, houses on a hill and a dirt path leading to a dark silhouette of people and a tree"></div>

<header>
  <div class="abs brand brand-top"><span class="dot"></span>flatmoveria.co.uk</div>
  <p class="abs tagline">The easiest way to swap your social home</p>
</header>

<form class="abs search">
  <label style="left:20px">Location</label>
  <label style="left:256px">Bedrooms</label>
  <label style="left:493px">Max Rent (per month)</label>
  <div class="field" style="left:20px">Town or postcode</div>
  <div class="field" style="left:256px"><span class="caret"></span></div>
  <div class="field" style="left:493px"><span class="caret"></span></div>
  <div class="search-btn">SEARCH</div>
</form>

<h1 class="abs headline">Join 500,000 other social tenants<br>on Larkfield Council House</h1>

<div class="abs role-buttons">
  <span class="role-tenant">Are you a tenant?Click here</span>
  <span class="role-landlord">Are you a landlord?Click here</span>
</div>

<section>
  <div class="abs need-card" style="left:195px;width:367px"></div>
  <div class="abs need-photo" role="img" aria-label="Illustration of a happy family waving in front of a house" style="left:58px;background:radial-gradient(circle at 50% 35%,#f4e6c8,#9ccf6a 75%)"></div>
  <p class="abs need-text" style="left:341px;top:795px">I need<br>More Space</p>

  <div class="abs need-card" style="left:744px;width:380px"></div>
  <div class="abs need-photo" role="img" aria-label="Illustration of a couple carrying boxes outside a house" style="left:606px;background:radial-gradient(circle at 50% 40%,#f2e3d0,#d8b89a 75%)"></div>
  <p class="abs need-text" style="left:891px;top:781px">I want to move<br>to a different<br>town</p>
</section>

<section>
  <h2 class="abs why">WHY CHOOSE<br>LARKFIELD COUNCIL HOUSE?</h2>

  <svg class="abs reason-mark" style="left:182px;top:1234px" viewBox="0 0 220 140" fill="none" stroke="#3bb54a" stroke-width="3">
    <circle cx="110" cy="70" r="63"/>
    <path d="M14 20 L34 10 L34 128 M22 128 L46 128"/>
    <circle cx="58" cy="17" r="5" fill="#3bb54a" stroke="none"/>
    <g stroke="#fff" stroke-width="2.2">
      <circle cx="110" cy="42" r="8"/>
      <path d="M98 76 v-18 q12-8 24 0 v18 M96 66 h28"/>
      <ellipse cx="110" cy="92" rx="10" ry="5"/>
      <ellipse cx="88" cy="82" rx="10" ry="5"/><ellipse cx="132" cy="82" rx="10" ry="5"/>
    </g>
  </svg>
  <p class="abs reason" style="left:137px;top:1392px;width:300px">Connect to thousands of other people in your area looking for a home swap</p>

  <svg class="abs reason-mark" style="left:551px;top:1234px" viewBox="0 0 220 140" fill="none" stroke="#3bb54a" stroke-width="3">
    <circle cx="110" cy="70" r="63"/>
    <path d="M6 38 q8-28 34-26 q28 4 14 34 L10 104 L60 104"/>
    <circle cx="70" cy="17" r="5" fill="#3bb54a" stroke="none"/>
    <g stroke="#fff" stroke-width="2.2">
      <rect x="80" y="40" width="60" height="42" rx="2"/>
      <path d="M104 82 v8 h12 v-8 M96 92 h28 M88 50 h20 M88 58 h16 M118 72 v-6 M124 72 v-10 M130 72 v-14"/>
    </g>
  </svg>
  <p class="abs reason" style="left:522px;top:1386px;width:260px">Our service is Completely free unlike most other exchange websites</p>

  <svg class="abs reason-mark" style="left:877px;top:1234px" viewBox="0 0 220 140" fill="none" stroke="#3bb54a" stroke-width="3">
    <circle cx="110" cy="70" r="63"/>
    <path d="M6 22 q22-18 44-4 q10 20-14 32 q30 6 20 38 q-18 20-48 4"/>
    <circle cx="70" cy="17" r="5" fill="#3bb54a" stroke="none"/>
    <g stroke="#fff" stroke-width="2.2">
      <rect x="80" y="42" width="58" height="48" rx="3"/>
      <path d="M80 54 h58 M88 38 v8 M100 38 v8 M112 38 v8 M124 38 v8"/>
      <path d="M88 62 h7 v7 h-7z M102 62 h7 v7 h-7z M116 62 h7 v7 h-7z M88 76 h7 v7 h-7z M102 76 h7 v7 h-7z M116 76 h7 v7 h-7z"/>
    </g>
  </svg>
  <p class="abs reason" style="left:842px;top:1386px;width:240px">Find an exchange<br>within 30 days!*</p>
</section>

<footer>
  <svg class="abs footer-edge" viewBox="0 0 1200 120" preserveAspectRatio="none">
    <path d="M0 60 Q600 -20 1200 60 L1200 120 L0 120Z" fill="#000"/>
  </svg>

  <h3 class="abs foot-head" style="left:207px">QUICK LINKS</h3>
  <ul class="abs foot-list" style="left:207px">
    <li>About Us</li><li>Terms of use</li><li>Privacy</li><li>Cookies</li><li>Ad privacy</li><li>Help</li>
  </ul>

  <h3 class="abs foot-head" style="left:484px">CONTACT INFO</h3>
  <div class="abs" style="left:484px;top:1808px;width:260px">
    <div class="contact-row">
      <svg width="13" height="16" viewBox="0 0 12 16"><path d="M6 0a6 6 0 0 1 6 6c0 4-6 10-6 10S0 10 0 6a6 6 0 0 1 6-6z" fill="#3bb54a"/><circle cx="6" cy="6" r="2.2" fill="#000"/></svg>
      <span>2322,Lorem ipsum dolor sitconse ctetur adipiscing elit,</span>
    </div>
    <div class="contact-row">
      <svg width="14" height="14" viewBox="0 0 14 14"><path d="M3 0l3 3-2 2q2 4 5 5l2-2 3 3-2 3Q3 13 0 3z" fill="#3bb54a"/></svg>
      <span>Call Us : 020 7946 0321</span>
    </div>
    <div class="contact-row">
      <svg width="16" height="12" viewBox="0 0 16 12"><rect width="16" height="12" rx="1" fill="#3bb54a"/><path d="M0 1l8 6 8-6" stroke="#000" stroke-width="1.4" fill="none"/></svg>
      <span>Info@flatmoveria.co.uk</span>
    </div>
  </div>

  <h3 class="abs foot-head" style="left:853px">HOURS</h3>
  <ul class="abs foot-list" style="left:853px;line-height:25px">
    <li>Mon&nbsp; : &nbsp;08:00 – 20:00</li><li>Tue&nbsp; : &nbsp;08:00 – 20:00</li><li>Wed&nbsp; : &nbsp;08:00 – 20:00</li><li>Thu&nbsp; : &nbsp;08:00 – 20:00</li><li>Fri&nbsp; : &nbsp;08:00 – 20:00</li><li>Sat&nbsp; : &nbsp;08:00 – 20:00</li><li>Sun&nbsp; : &nbsp;Closed</li>
  </ul>

  <div class="abs brand brand-foot"><span class="dot"></span>flatmoveria.co.uk</div>

  <span class="abs social" style="left:796px" aria-label="Social profile"></span>
  <span class="abs social" style="left:848px" aria-label="Social profile"></span>
  <span class="abs social" style="left:900px" aria-label="Social profile"></span>
  <span class="abs social" style="left:952px" aria-label="Social profile"></span>

  <p class="abs copyright">Copyright © 2020 Flatmoveria - All Rights Reserved.</p>
</footer>
</body>
</html>
```